Refresh of The Marston Collective business card

Update business card design using existing primary logo. Names, numbers, etc. are too hard to read on current design.

Target Market(s)

We are a CPA firm.

Industry/Entity Type

Accountant

Contact Information for Business Card

update current card

Colors
0355a3
3176b5
85acd3
0792cd

Requirements
Must have
• Easier to read phone numbers and names
• Use existing logo
Nice to have
• We love our color scheme and current TMC logo. But the names and phone numbers are too small and card just look old and stale.

```html
<!DOCTYPE html>
<html lang="en">
<head>
<meta charset="utf-8">
<title>The Marston Collective – Business Card</title>
<link href="https://fonts.googleapis.com/css2?family=Arimo:wght@400;700&family=Roboto+Condensed:wght@700&display=swap" rel="stylesheet">
<style>
  :root {
    --brand-navy: #0355a3;
    --brand-mid: #3176b5;
    --brand-light: #85acd3;
    --brand-sky: #0792cd;
    --ring-grey: #555a5f;
    --text-grey: #4a4d50;
    --card-white: #f3f3f3;
    --backdrop: #2a2a2a;
  }
  * { margin: 0; padding: 0; box-sizing: border-box; }
  html, body { width: 1200px; height: 960px; overflow: hidden; }
  body {
    background: var(--backdrop);
    font-family: "Arimo", Arial, sans-serif;
    position: relative;
  }
  .card {
    position: absolute;
    left: 300px;
    width: 600px;
    height: 342px;
    border-radius: 18px;
    background: var(--card-white);
    overflow: hidden;
    box-shadow: 0 4px 10px rgba(0,0,0,.5);
  }
  .card--front { top: 124px; }
  .card--back { top: 493px; }
  .card__art { position: absolute; inset: 0; width: 600px; height: 342px; }

  .wordmark {
    display: flex;
    align-items: center;
    gap: 12px;
    position: absolute;
  }
  .wordmark__dot {
    border-radius: 50%;
    background: var(--brand-navy);
    flex: none;
  }
  .wordmark__name {
    color: var(--brand-navy);
    font-weight: 700;
    text-transform: uppercase;
    line-height: 1.05;
  }
  .tagline {
    color: var(--text-grey);
    font-size: 8px;
    letter-spacing: 1.6px;
    text-transform: uppercase;
  }

  .card--front .wordmark { left: 26px; top: 24px; }
  .card--front .wordmark__dot { width: 76px; height: 76px; }
  .card--front .wordmark__name { font-size: 17px; }
  .card--front .tagline { position: absolute; left: 114px; top: 88px; }

  .holder {
    position: absolute;
    left: 24px;
    top: 117px;
    color: var(--brand-navy);
    font-family: "Roboto Condensed", "Arial Narrow", sans-serif;
    font-size: 22px;
    font-weight: 700;
    letter-spacing: .2px;
    white-space: nowrap;
  }
  .address {
    position: absolute;
    left: 25px;
    top: 153px;
    color: var(--text-grey);
    font-size: 18px;
    line-height: 23px;
    font-style: normal;
  }
  .contacts {
    position: absolute;
    left: 26px;
    top: 228px;
    list-style: none;
    color: var(--text-grey);
    font-size: 18px;
    line-height: 22.7px;
  }
  .contacts li { display: flex; align-items: center; gap: 8px; }
  .contacts svg { width: 16px; height: 16px; fill: var(--brand-navy); flex: none; }

  .card--back .wordmark { right: 34px; top: 184px; }
  .card--back .wordmark__dot { width: 30px; height: 30px; }
  .card--back .wordmark__name { font-size: 26px; text-align: right; }
  .card--back .tagline { position: absolute; right: 34px; top: 280px; font-size: 9px; }
  .website {
    position: absolute;
    right: 33px;
    top: 293px;
    color: var(--text-grey);
    font-family: "Roboto Condensed", "Arial Narrow", sans-serif;
    font-size: 20px;
    font-weight: 700;
  }
</style>
</head>
<body>

<section class="card card--front" aria-label="Business card front">
  <svg class="card__art" viewBox="0 0 600 342" aria-hidden="true">
    <defs>
      <radialGradient id="discFront" cx="0.45" cy="0.4" r="0.65">
        <stop offset="0" stop-color="var(--brand-mid)"/>
        <stop offset="0.6" stop-color="var(--brand-navy)"/>
        <stop offset="1" stop-color="#033f7c"/>
      </radialGradient>
    </defs>
    <circle cx="470" cy="172" r="182" fill="var(--ring-grey)"/>
    <circle cx="480" cy="172" r="175" fill="url(#discFront)"/>
  </svg>

  <div class="wordmark">
    <span class="wordmark__dot"></span>
    <span class="wordmark__name">The Marston<br>Collective</span>
  </div>
  <p class="tagline">Certified Public Accountants</p>

  <h1 class="holder">DANIEL R. MARSTON, CPA</h1>
  <address class="address">812 W. Orchard Ave.<br>Suite 310<br>Lakemont, Florida 32799</address>
  <ul class="contacts">
    <li><svg viewBox="0 0 16 16"><path d="M3.5 1.5l2.5 0 1 3.5-1.6 1.2a8 8 0 0 0 4.4 4.4L11 9l3.5 1v2.5c0 1-1 2-2 2C6.5 14.5 1.5 9.5 1.5 3.5c0-1 1-2 2-2z"/></svg>407.555.0142</li>
    <li><svg viewBox="0 0 16 16"><path d="M4.5 0.5h7a1 1 0 0 1 1 1v13a1 1 0 0 1-1 1h-7a1 1 0 0 1-1-1v-13a1 1 0 0 1 1-1zm0.8 2v10h5.4v-10z"/></svg>407.555.0187</li>
    <li><svg viewBox="0 0 16 16"><path d="M4 1h7l1 1v4H4zM1.5 7h13a1 1 0 0 1 1 1v5a1 1 0 0 1-1 1h-13a1 1 0 0 1-1-1V8a1 1 0 0 1 1-1zm2 2v1.5h9V9z"/></svg>407.555.0163</li>
    <li><svg viewBox="0 0 16 16"><path d="M1 3.5h14v9H1zm1.4 1l5.6 4.2 5.6-4.2z"/></svg>dan@marstoncollective.com</li>
  </ul>
</section>

<section class="card card--back" aria-label="Business card back">
  <svg class="card__art" viewBox="0 0 600 342" aria-hidden="true">
    <defs>
      <radialGradient id="discBack" cx="0.45" cy="0.4" r="0.65">
        <stop offset="0" stop-color="var(--brand-mid)"/>
        <stop offset="0.6" stop-color="var(--brand-navy)"/>
        <stop offset="1" stop-color="#033f7c"/>
      </radialGradient>
    </defs>
    <circle cx="138" cy="176" r="180" fill="var(--ring-grey)"/>
    <circle cx="128" cy="176" r="175" fill="url(#discBack)"/>
  </svg>

  <div class="wordmark">
    <span class="wordmark__dot"></span>
    <span class="wordmark__name">The Marston<br>Collective</span>
  </div>
  <p class="tagline">Certified Public Accountants</p>
  <p class="website">www.marstoncollective.com</p>
</section>

</body>
</html>
```